Modern Website For Law Firm Lawyer Melbourne, Australia Coded

We are looking for a modern and sophisticated website design. We would prefer the site to be based on WordPress given it is intuitive and some of our staff have experience using it.

Our law firm is based in Melbourne, Australia and we deal with property. The website must be hosted on a reliable Australian server.

We would also appreciate it if the designer can provide some guidance about how to make changes/upload content, such as photos and articles. We are happy to pay for this advice.

We prefer classic fonts in black or grey. We would also like a dash of colour so please use a green, blue or aqua colour palette that is consistent with our logo attached.

We do not want any law related images - scales of justice, gavel or the like.

Our ultimate goal is to communicate that the firm is professional, affordable, modern, dynamic, knowledgeable and one with the community.

We would like the following pages/sections/icons:

1. Who We Are - we will provide content.

2. Our Services - 1. Property 2. Wills, 3. Powers of Attorney 4. Probate & Estate Administration 5.Consultancy & Agency- we will provide content for each of these sections.

3. Articles - we already have approximately 20 articles on a wordpress blog and would like to port these articles to the website. We can do this ourselves if the designer can give us instructions about how to do this. We would also like to give clients the option to subscribe to our articles.

4. Contact Us - this should include our firms contact details; location map and we would like to give clients the option to "Request A Quote" directly from the page - i.e they will need to provide their full name, phone number email address, choose subject from drop down menu and type a message that gets sent to our outlook email.

5. Terms and Conditions - we will provide content

We really like the style and photographs used in the following website and want something as close to this as possible:

https://www.brellwick.com/

For privacy reasons, we would prefer to provide content together with all business details once we have decided on the winner.

We will monitor entries closely and promise to provide feedback and guidance on each entry.

This project is guaranteed. If our budget is too low please email us so we can discuss further and perhaps increase our budget. We are reasonable in this regard.

Thank you very much for considering this project.

Target Market(s)

General public, professionals, lawyers and conveyancers

Industry/Entity Type

Law Firm

Coding

Coded - Design and coding required

Number of Pages Required

1 page

Font styles to use
Sans Serif

Colors
33b8a4
33a6d7
0692cd
3176b5
00a990
9bcb3c
86cfc6
cadf82
85acd3

Requirements
Must have
• 1. Site must be coded and hosted on a reliable Australian server and it would be much appreciated if the deisgner provides instructions about how to add photos, blog articles etc-
• 2. The site must be secure and have green lock at top of page
• 3. Request A Quote - name, email, phone, drop down subject, message - email to our outlook email
• 4. Article Subscription
• 5. Domain (we have already purchased)
• 6. Location map
• 7. Facebook, LinkedIn, Instagram Icons
• 8. Membership icons in this order - VLQ Member > Coastal Women Advocates > Guidance Through Counsel > Fernmoor Society > Tolvo > Kestrimail > Wex KY logos attached to go on bottom of page
• 9. Testimonials
Nice to have
• A modern, sophisticated website like:
• https://www.brellwick.com/ - we really like the style of the brellwick photographs
• We also really like this design by Qt of Sketch hive:
• https://www.sketchhive.com.au/design/58210643
Should not have
• Law related images - scales of justice gavel and the like

```html
<!DOCTYPE html>
<html lang="en">
<head>
<meta charset="utf-8">
<title>Ridgeline Lawyers</title>
<link href="https://fonts.googleapis.com/css2?family=Roboto:wght@300;400;500;700&family=Roboto+Condensed:wght@300;400&display=swap" rel="stylesheet">
<style>
:root{
  --green:#9bcb3c;
  --green-dark:#86b82e;
  --aqua:#33b8c4;
  --blue:#0692cd;
  --blue-dark:#3176b5;
  --ink:#333;
  --grey:#666;
  --light:#f2f2f2;
  --night:#1c1c1c;
  --white:#fff;
}
*{box-sizing:border-box;margin:0;padding:0}
html,body{width:1200px;height:3789px;overflow:hidden}
body{font-family:"Roboto",Arial,sans-serif;color:var(--ink);background:var(--white);position:relative}
section,header,footer{position:absolute;left:0;width:1200px}
.abs{position:absolute}
.photo{position:absolute}
.section-title{position:absolute;left:0;width:1200px;text-align:center;font-family:"Roboto Condensed",Arial,sans-serif;font-weight:300;font-size:30px;letter-spacing:1px;text-transform:uppercase}
.section-title::before{content:"";display:block;width:50px;height:3px;margin:0 auto 14px;background:var(--aqua)}

/* header */
.hero{top:0;height:625px;overflow:hidden}
.hero .photo{inset:0;background:linear-gradient(100deg,#f4f6f7 0%,#dfe4e8 45%,#9aa3ab 70%,#4c5662 100%)}
.navbar{position:absolute;left:115px;top:36px;width:970px;height:86px;background:var(--white);box-shadow:0 2px 8px rgba(0,0,0,.12)}
.brand{position:absolute;left:22px;top:24px;display:flex;align-items:center;gap:10px;font-size:15px;color:var(--ink);letter-spacing:1px;text-transform:uppercase}
.brand i{width:34px;height:34px;border-radius:50%;background:var(--aqua);display:block}
.topbar{position:absolute;left:272px;top:0;width:698px;height:30px;background:var(--green);color:var(--white);font-size:12px;display:flex;align-items:center;padding:0 14px;gap:28px}
.topbar .social{margin-left:auto;display:flex;gap:10px}
.topbar .social span{width:12px;height:12px;background:var(--white);border-radius:2px;display:block}
.menu{position:absolute;left:272px;top:44px;display:flex;font-size:13px;align-items:center}
.menu a{color:var(--ink);text-decoration:none;padding:8px 17px}
.menu a.active{color:var(--blue);border-bottom:2px solid var(--blue)}
.menu .quote{background:var(--blue-dark);color:var(--white);padding:9px 14px;margin-left:8px;border-radius:2px}
.hero-title{position:absolute;left:112px;top:228px;color:var(--aqua);font-family:"Roboto Condensed",Arial,sans-serif;font-weight:300;text-transform:uppercase;line-height:1}
.hero-title .l1{display:block;font-size:52px;letter-spacing:9px}
.hero-title .l2{display:block;font-size:92px;letter-spacing:7px;margin-top:4px}
.hero-text{position:absolute;left:112px;top:392px;width:450px;font-size:13px;line-height:1.5;color:var(--ink)}
.btn{display:inline-block;background:var(--aqua);color:var(--white);font-size:14px;padding:12px 26px;text-decoration:none}
.hero .btn{position:absolute;left:112px;top:456px}
.dots{position:absolute;left:112px;top:588px;display:flex;gap:8px}
.dots span{width:28px;height:3px;background:#9aa;display:block}
.dots span:first-child{background:var(--aqua)}

/* who we are */
.who{top:625px;height:495px;background:var(--white)}
.who .p1{left:252px;top:95px;width:390px;height:180px;background:linear-gradient(120deg,#9b5a44,#c7b7a4 55%,#5c6e86);box-shadow:0 4px 12px rgba(0,0,0,.2)}
.who .p2{left:112px;top:242px;width:325px;height:178px;background:linear-gradient(120deg,#2d4f88,#6d87b0 50%,#26313f);box-shadow:0 4px 12px rgba(0,0,0,.25);border:4px solid var(--white)}
.who h2{position:absolute;left:678px;top:90px;font-family:"Roboto Condensed",Arial,sans-serif;font-weight:300;font-size:30px;letter-spacing:1px}
.who h2::before{content:"";display:block;width:50px;height:3px;margin-bottom:14px;background:var(--aqua)}
.who p{position:absolute;left:678px;width:405px;font-size:12.5px;line-height:1.6;color:var(--grey)}

/* services */
.services{top:1120px;height:695px;background:linear-gradient(120deg,var(--green) 0%,#a9d34f 50%,var(--green-dark) 100%);overflow:hidden}
.services .shade{position:absolute;inset:0}
.services .section-title{top:95px;color:var(--white)}
.services .section-title::before{background:var(--white)}
.card{position:absolute;background:var(--white);text-align:center;padding:30px 22px 0;box-shadow:0 4px 14px rgba(0,0,0,.15)}
.card .tab{position:absolute;left:50%;top:-22px;width:56px;height:24px;margin-left:-28px;background:var(--white);border-radius:28px 28px 0 0}
.card svg{position:absolute;left:50%;top:-16px;margin-left:-12px}
.card h3{font-size:15px;font-weight:500;text-transform:uppercase;margin-bottom:14px;line-height:1.3}
.card p{font-size:12px;line-height:1.6;color:var(--grey)}

/* articles */
.articles{top:1815px;height:645px}
.articles .section-title{top:95px}
.art-grid{position:absolute;left:112px;top:162px;width:975px;height:408px}
.art-text{position:absolute;background:var(--white);padding:24px;font-size:12px;color:var(--grey);line-height:1.55}
.art-text h4{font-size:15px;color:var(--ink);font-weight:500;margin-bottom:10px}
.art-text a{color:var(--blue);text-decoration:none;display:block;margin-top:14px;font-size:13px}
.art-text.feature{background:var(--blue);color:#e4f3fa}
.art-text.feature h4,.art-text.feature a{color:var(--white)}

/* testimonials */
.testimonials{top:2460px;height:490px;background:var(--aqua);overflow:hidden}
.testimonials .section-title{top:80px;color:var(--white)}
.testimonials .section-title::before{background:var(--white)}
.quote-card{position:absolute;top:152px;width:305px;background:var(--white);padding:24px 22px;box-shadow:0 4px 14px rgba(0,0,0,.15)}
.quote-card .who-row{display:flex;gap:12px;align-items:center;margin-bottom:22px}
.quote-card .avatar{width:44px;height:44px;border-radius:50%;background:linear-gradient(135deg,#8a97a6,#3d4652);flex:none}
.quote-card h5{font-size:12px;font-weight:500;text-transform:uppercase}
.quote-card small{font-size:10px;color:var(--grey)}
.quote-card p{font-size:12.5px;line-height:1.6;color:var(--grey)}
.stars{color:#e0a82e;font-size:14px;letter-spacing:2px;margin-top:10px}

/* memberships */
.members{top:2950px;height:115px;background:#dedede;display:flex;align-items:center;justify-content:center;gap:58px}
.badge{width:96px;height:44px;background:#b7b7b7;border-radius:4px}
.badge.round{width:60px;height:60px;border-radius:50%}

/* contact */
.contact{top:3065px;height:724px;background:linear-gradient(to bottom,var(--white) 0,var(--white) 247px,var(--night) 247px)}
.contact .section-title{top:90px}
.map{position:absolute;left:112px;top:170px;width:975px;height:420px;background:linear-gradient(135deg,#e6e6e6,#cfcfcf 60%,#e1e1e1)}
.info-bar{position:absolute;left:150px;top:525px;width:925px;height:100px;background:var(--white);display:flex;align-items:center;box-shadow:0 4px 16px rgba(0,0,0,.2)}
.info{flex:1;display:flex;align-items:center;gap:14px;padding:0 22px;border-right:1px solid #ddd;height:60px}
.info:last-child{border:none}
.info b{display:block;color:var(--blue);font-weight:400;font-size:17px;margin-bottom:4px}
.info span{font-size:12.5px;color:var(--ink)}
.follow{display:flex;gap:6px;margin-top:4px}
.follow i{width:28px;height:28px;border-radius:50%;display:block}
.footer{position:absolute;left:112px;top:686px;width:975px;display:flex;justify-content:space-between;font-size:11px;color:#bbb}
.footer em{font-style:normal;color:var(--aqua)}
</style>
</head>
<body>

<header class="hero">
  <div class="photo" role="img" aria-label="Photo of a lawyer in glasses and a suit working at a laptop in a bright office"></div>
  <div class="navbar">
    <div class="brand"><i></i>Ridgeline<br>Lawyers</div>
    <div class="topbar"><span>Call : +(61) 200 555 014</span><span>Email : info@ridgelinelawyers.com</span><div class="social"><span></span><span></span><span></span><span></span></div></div>
    <nav class="menu">
      <a class="active">Home</a><a>Who We Are</a><a>Our Services</a><a>Articles</a><a>Testimonials</a><a>Contact Us</a><a class="quote">Request A Quote</a>
    </nav>
  </div>
  <h1 class="hero-title"><span class="l1">Ridgeline</span><span class="l2">Lawyers</span></h1>
  <p class="hero-text">Lorem ipsum dolor sit amet, consectetur adipiscing elit, sed do eiusmod tempor incididunt ut labore et dolore magna aliqua.</p>
  <a class="btn">Read More »</a>
  <div class="dots"><span></span><span></span><span></span></div>
</header>

<section class="who">
  <div class="photo p1" role="img" aria-label="Photo of a smiling couple meeting a lawyer outside a brick home"></div>
  <div class="photo p2" role="img" aria-label="Photo of business people shaking hands in a meeting"></div>
  <h2>WHO WE ARE</h2>
  <p style="top:150px">But I must explain to you how all this mistaken idea of denouncing pleasure and praising pain was born and I will give you a complete account of the system, and expound the actual teachings of the great explorer of the truth, the master-builder of human happiness. No one rejects, dislikes, or avoids pleasure itself, because it is pleasure.</p>
  <p style="top:272px">At vero eos et accusamus et iusto odio dignissimos ducimus qui blanditiis praesentium voluptatum deleniti atque corrupti quos dolores et quas moles- tias excepturi sint occaecati cupiditate non provident, similique sunt in culpa qui officia deserunt mollitia anim.</p>
</section>

<section class="services">
  <div class="shade" role="img" aria-label="Soft green-tinted photo of an office meeting room"></div>
  <svg class="abs" style="left:0;top:0" width="1200" height="695" aria-hidden="true"><polygon points="0,380 0,695 420,695" fill="rgba(255,255,255,.12)"/><polygon points="640,0 1200,0 1200,420" fill="rgba(0,0,0,.05)"/></svg>
  <h2 class="section-title">Our Services</h2>

  <div class="card" style="left:112px;top:200px;width:275px;height:168px"><span class="tab"></span>
    <svg width="24" height="24" viewBox="0 0 24 24" fill="none" stroke="#33b8c4" stroke-width="1.6"><path d="M3 11l9-7 9 7M6 10v10h12V10"/></svg>
    <h3>Property</h3><p>Sed ut perspiciatis unde omnis iste natus error sit voluptatem accusantium doloremque laudantium totam rem aperiam.</p></div>
  <div class="card" style="left:450px;top:200px;width:275px;height:168px"><span class="tab"></span>
    <svg width="24" height="24" viewBox="0 0 24 24" fill="none" stroke="#33b8c4" stroke-width="1.6"><rect x="5" y="3" width="14" height="18"/><path d="M8 8h8M8 12h8M8 16h5"/></svg>
    <h3>Wills</h3><p>Sed ut perspiciatis unde omnis iste natus error sit voluptatem accusantium doloremque laudantium totam rem aperiam.</p></div>
  <div class="card" style="left:787px;top:200px;width:300px;height:168px"><span class="tab"></span>
    <svg width="24" height="24" viewBox="0 0 24 24" fill="none" stroke="#33b8c4" stroke-width="1.6"><path d="M6 3h9l4 4v14H6z"/><path d="M9 12h7M9 16h7"/></svg>
    <h3>Powers of Attorney</h3><p>Sed ut perspiciatis unde omnis iste natus error sit voluptatem accusantium doloremque laudantium totam rem aperiam.</p></div>
  <div class="card" style="left:282px;top:420px;width:300px;height:200px"><span class="tab"></span>
    <svg width="24" height="24" viewBox="0 0 24 24" fill="none" stroke="#33b8c4" stroke-width="1.6"><circle cx="12" cy="8" r="4"/><path d="M4 21c1-5 15-5 16 0"/></svg>
    <h3>Probate &amp;<br>Estate Administration</h3><p>Sed ut perspiciatis unde omnis iste natus error sit voluptatem accusantium doloremque laudantium totam rem aperiam.</p></div>
  <div class="card" style="left:620px;top:420px;width:300px;height:170px"><span class="tab"></span>
    <svg width="24" height="24" viewBox="0 0 24 24" fill="none" stroke="#33b8c4" stroke-width="1.6"><rect x="4" y="8" width="16" height="12"/><path d="M9 8V5h6v3"/></svg>
    <h3>Consultancy &amp; Agency</h3><p>Sed ut perspiciatis unde omnis iste natus error sit voluptatem accusantium doloremque laudantium totam rem aperiam.</p></div>
</section>

<section class="articles">
  <h2 class="section-title">Latest Article</h2>
  <div class="art-grid">
    <div class="photo" style="left:0;top:0;width:245px;height:200px;background:linear-gradient(130deg,#8fb4d6,#4b6b8e 55%,#c9d8e4)" role="img" aria-label="Photo of colleagues shaking hands in an office"></div>
    <div class="art-text" style="left:245px;top:0;width:245px;height:200px"><h4>Lorem ipsum dolor sit amet.</h4>Sed ut perspiciatis unde omnis iste natus error sit voluptatem accusantium doloremque laudantium, totam rem aperiam.<a>Read More »</a></div>
    <div class="art-text" style="left:0;top:200px;width:245px;height:208px"><h4>Lorem ipsum dolor sit amet.</h4>Sed ut perspiciatis unde omnis iste natus error sit voluptatem accusantium doloremque laudantium, totam rem aperiam.<a>Read More »</a></div>
    <div class="photo" style="left:245px;top:200px;width:245px;height:208px;background:linear-gradient(130deg,#e9eef2,#7d8c99 55%,#2e3844)" role="img" aria-label="Photo of a man working on a laptop by a window"></div>
    <div class="photo" style="left:490px;top:0;width:485px;height:408px;background:linear-gradient(110deg,#a57d55,#d9cfc2 45%,#4a5a6c 75%,#e6e8ea)" role="img" aria-label="Photo of a bearded lawyer in glasses working at a desk in a library office"></div>
    <div class="art-text feature" style="left:490px;top:230px;width:255px;height:178px"><h4>Lorem ipsum dolor sit amet.</h4>Sed ut perspiciatis unde omnis iste natus error sit voluptatem accusantium doloremque laudantium, totam rem aperiam.<a>Read More »</a></div>
  </div>
</section>

<section class="testimonials">
  <h2 class="section-title">Testimonials</h2>
  <div class="quote-card" style="left:112px"><div class="who-row"><div class="avatar" role="img" aria-label="Client portrait"></div><div><h5>Lorem ipsum dolor sit amet</h5><small>Sed ut perspiciatis</small></div></div>
    <p>But I must explain to you how all this mistaken idea of denouncing pleasure and praising pain was born and I will give you a complete ac- count of the system.</p><div class="stars">★★★★★</div></div>
  <div class="quote-card" style="left:447px;top:145px"><div class="who-row"><div class="avatar" role="img" aria-label="Client portrait"></div><div><h5>Lorem ipsum dolor sit amet</h5><small>Sed ut perspiciatis</small></div></div>
    <p>But I must explain to you how all this mistaken idea of denouncing pleasure and praising pain was born and I will give you a complete ac- count of the system, and expound the actual teachings of the great explorer.</p><div class="stars">★★★★★</div></div>
  <div class="quote-card" style="left:782px"><div class="who-row"><div class="avatar" role="img" aria-label="Client portrait"></div><div><h5>Lorem ipsum dolor sit amet</h5><small>Sed ut perspiciatis</small></div></div>
    <p>But I must explain to you how all this mistaken idea of denouncing pleasure and praising pain was born and I will give.</p><div class="stars">★★★★★</div></div>
</section>

<section class="members" aria-label="Memberships">
  <span class="badge"></span><span class="badge"></span><span class="badge"></span><span class="badge round"></span><span class="badge"></span><span class="badge"></span><span class="badge"></span>
</section>

<section class="contact">
  <h2 class="section-title">Contact Us</h2>
  <div class="map" role="img" aria-label="Greyscale street map showing the office location"></div>
  <svg class="abs" style="left:584px;top:330px" width="28" height="38" viewBox="0 0 28 38" aria-hidden="true"><path d="M14 0C6 0 0 6 0 14c0 10 14 24 14 24s14-14 14-24C28 6 22 0 14 0z" fill="#555"/><circle cx="14" cy="14" r="5" fill="#ddd"/></svg>
  <div class="info-bar">
    <div class="info"><svg width="30" height="36" viewBox="0 0 28 38"><path d="M14 0C6 0 0 6 0 14c0 10 14 24 14 24s14-14 14-24C28 6 22 0 14 0z" fill="#e5533d"/><circle cx="14" cy="14" r="5" fill="#fff"/></svg><div><b>Address</b><span>Harbourvale Road 184</span></div></div>
    <div class="info"><svg width="30" height="30" viewBox="0 0 24 24"><path d="M6 2h5l2 5-3 2c1 3 3 5 6 6l2-3 5 2v5c0 1-1 2-2 2C10 21 3 14 3 4c0-1 1-2 3-2z" fill="#3176b5"/></svg><div><b>Phone</b><span>+61 200 555 014</span></div></div>
    <div class="info"><svg width="32" height="26" viewBox="0 0 32 26"><rect x="1" y="3" width="30" height="22" fill="#e0a82e"/><path d="M1 3l15 12L31 3" fill="none" stroke="#fff" stroke-width="2"/></svg><div><b>Email</b><span>hello@ridgelinelawyers.com</span></div></div>
    <div class="info"><div><b>Follo Us</b><div class="follow"><i style="background:#3b5998"></i><i style="background:#33a6d7"></i><i style="background:#dd4b39"></i><i style="background:#e5533d"></i><i style="background:#0692cd"></i></div></div></div>
  </div>
  <footer class="footer"><span>Copyright © 2017 <em>GUIDANCE THROUGH COUNSEL</em> All Rights Reserved</span><span>Terms and Conditions</span></footer>
</section>

</body>
</html>
```